Real Estate Sign

My company is in need of a redesign for our real estate lawn sign. The sign should show our logo, the phrase "For Sale", our phone number 410-587-3391 and website www.HomeKeelTX.com.
Updates

Hello

Thank you for your submissions.  I am looking for the website and phone number to be very visible from a good distance.  I do also want to stay within the colors of my logo. Too many colors could be expensive to reproduce.

Thank you
Gordon

I favor clean, straight lines and design.  I prefer not to add any other graphics or logos on the sign.  The logo and name are enough. I am looking for readability from a good distance and prefer calls to action like call 410-593-3391 for information or visit www.HomeKeelTX.com to schedule tour today!  I don't really need FOR SALE to be so prominent.

thanks for all the submissions.
Gordon

Gordon

Industry/Entity Type

Real Estate

```html
<!DOCTYPE html>
<html lang="en">
<head>
<meta charset="UTF-8">
<title>HomeKeel Realty – Lawn Sign</title>
<link rel="stylesheet" href="https://fonts.googleapis.com/css2?family=Montserrat:wght@500&family=Open+Sans:wght@300;400&display=swap">
<style>
  :root {
    --page: #ffffff;
    --accent: #00b2f4;
    --panel-light: #1269b2;
    --panel-dark: #0a4778;
    --band: #073868;
    --ink: #ffffff;
  }
  * { margin: 0; padding: 0; box-sizing: border-box; }
  html, body {
    width: 1200px;
    height: 900px;
    overflow: hidden;
    background: var(--page);
  }
  .sign {
    position: absolute;
    left: 35px;
    top: 107px;
    width: 1122px;
    height: 690px;
    background: var(--band);
    box-shadow: 0 1px 4px rgba(0, 0, 0, 0.25);
    overflow: hidden;
  }
  .sale-bar {
    position: absolute;
    left: 0;
    top: 0;
    width: 138px;
    height: 100%;
    background: var(--accent);
  }
  .sale-bar__label {
    position: absolute;
    left: 69px;
    top: 345px;
    transform: translate(-50%, -50%) rotate(-90deg);
    white-space: nowrap;
    font-family: "Montserrat", sans-serif;
    font-weight: 500;
    font-size: 92px;
    letter-spacing: 8px;
    color: var(--ink);
  }
  .brand-panel {
    position: absolute;
    left: 138px;
    top: 0;
    width: 984px;
    height: 406px;
    background: radial-gradient(ellipse 55% 60% at 50% 62%, var(--panel-light) 0%, var(--panel-dark) 100%);
  }
  .brand {
    position: absolute;
    left: 0;
    right: 0;
    top: 190px;
    text-align: center;
    font-family: "Open Sans", sans-serif;
    font-weight: 400;
    color: var(--ink);
  }
  .brand__name {
    display: block;
    font-size: 118px;
    line-height: 1;
    letter-spacing: -2px;
  }
  .brand__type {
    display: block;
    margin-top: 30px;
    font-size: 46px;
    letter-spacing: 22px;
    line-height: 1;
  }
  .contact {
    position: absolute;
    left: 138px;
    top: 406px;
    width: 984px;
    height: 284px;
    text-align: center;
    font-family: "Open Sans", sans-serif;
    color: var(--ink);
  }
  .contact__prompt {
    position: absolute;
    left: 0; right: 0;
    top: 36px;
    font-weight: 300;
    font-size: 37px;
    letter-spacing: 1px;
  }
  .contact__phone {
    position: absolute;
    left: 0; right: 0;
    top: 82px;
    font-weight: 400;
    font-size: 96px;
    line-height: 1.1;
    letter-spacing: 1px;
  }
  .contact__web {
    position: absolute;
    left: 0; right: 0;
    top: 180px;
    font-weight: 400;
    font-size: 62px;
    letter-spacing: 2px;
  }
</style>
</head>
<body>
  <div class="sign">
    <div class="sale-bar">
      <span class="sale-bar__label">FOR SALE</span>
    </div>
    <div class="brand-panel">
      <div class="brand">
        <span class="brand__name">HomeKeel</span>
        <span class="brand__type">REALTY</span>
      </div>
    </div>
    <div class="contact">
      <p class="contact__prompt">Please contact us for more information</p>
      <p class="contact__phone">410-593-3391</p>
      <p class="contact__web">www.HomeKeelTX.com</p>
    </div>
  </div>
</body>
</html>
```